Varnel Supply requires a new business card.

We are an online professional tool store.

Target Market(s)

We target the professional technician.

Industry/Entity Type

Business

Contact Information for Business Card

VarnelSupply.com.au

sales@varnelsupply.example

Requirements
Must have
• Needs to look commercial and professional
Should not have
• No Australian Colors, maps or shapes.
• No Shapes of Tools

```html
<!DOCTYPE html>
<html lang="en">
<head>
<meta charset="utf-8">
<title>Varnel Supply business card</title>
<link href="https://fonts.googleapis.com/css2?family=Questrial&display=swap" rel="stylesheet">
<style>
  :root {
    --page: #e6e6e9;
    --navy-deep: #16206a;
    --navy: #23308a;
    --navy-mid: #2e3d9a;
    --silver: #dcdde2;
    --silver-light: #f1f1f4;
    --ink-light: #e4e6f2;
    --brand: #141c5e;
  }
  html, body {
    margin: 0;
    padding: 0;
    width: 1200px;
    height: 970px;
    overflow: hidden;
    background: var(--page);
    font-family: "Questrial", "Century Gothic", sans-serif;
  }
  .business-card {
    position: absolute;
    left: 80px;
    top: 188px;
    width: 1040px;
    height: 594px;
    overflow: hidden;
    box-shadow: 0 14px 40px rgba(20, 24, 60, 0.25);
  }
  .card-art {
    position: absolute;
    inset: 0;
  }
  .holder {
    position: absolute;
    left: 55px;
    color: var(--ink-light);
  }
  .holder-name {
    top: 86px;
    margin: 0;
    font-size: 36px;
    font-weight: 400;
    letter-spacing: 0.2px;
  }
  .holder-role {
    top: 128px;
    margin: 0;
    font-size: 24px;
  }
  .postal-address {
    position: absolute;
    left: 55px;
    top: 262px;
    margin: 0;
    font-style: normal;
    font-size: 24px;
    line-height: 33px;
    color: var(--ink-light);
  }
  .contact-list {
    position: absolute;
    left: 55px;
    top: 356px;
    margin: 0;
    padding: 0;
    list-style: none;
    color: var(--ink-light);
    font-size: 25px;
  }
  .contact-item {
    display: flex;
    align-items: center;
    height: 36px;
  }
  .contact-icon {
    width: 32px;
    height: 32px;
    margin-right: 16px;
    flex: none;
  }
  .brand-name {
    position: absolute;
    left: 560px;
    width: 480px;
    top: 268px;
    margin: 0;
    text-align: center;
    font-size: 48px;
    font-weight: 400;
    color: var(--brand);
    letter-spacing: 0.5px;
  }
</style>
</head>
<body>
  <div class="business-card">
    <svg class="card-art" width="1040" height="594" viewBox="0 0 1040 594" aria-hidden="true">
      <defs>
        <linearGradient id="card-surface" x1="0" y1="0" x2="1" y2="0">
          <stop offset="0" stop-color="#1c2779"/>
          <stop offset="0.25" stop-color="#2a3892"/>
          <stop offset="0.38" stop-color="#25328a"/>
          <stop offset="0.44" stop-color="#8e94bf"/>
          <stop offset="0.5" stop-color="#d6d7de"/>
          <stop offset="1" stop-color="#e9e9ed"/>
        </linearGradient>
        <radialGradient id="inner-glow" cx="0.5" cy="0.5" r="0.5">
          <stop offset="0" stop-color="#f4f4f7"/>
          <stop offset="1" stop-color="#d3d4db"/>
        </radialGradient>
      </defs>
      <rect class="card-surface" width="1040" height="594" fill="url(#card-surface)"/>
      <circle class="inner-disc" cx="805" cy="300" r="270" fill="url(#inner-glow)"/>
      <path class="crescent-ring" fill="var(--navy-deep)" fill-rule="evenodd"
        d="M 454 296 a 316 316 0 1 0 632 0 a 316 316 0 1 0 -632 0 Z
           M 535 300 a 270 270 0 1 0 540 0 a 270 270 0 1 0 -540 0 Z"/>
    </svg>

    <h1 class="holder holder-name">Mara Quinlan</h1>
    <p class="holder holder-role">Founder</p>

    <address class="postal-address">PO BOX 123 your address<br>2nd street Melbourne</address>

    <ul class="contact-list">
      <li class="contact-item">
        <svg class="contact-icon" viewBox="0 0 32 32" fill="none" stroke="currentColor" stroke-width="1.4">
          <circle cx="16" cy="16" r="14.5"/>
          <rect x="11.5" y="8" width="9" height="16" rx="1.5"/>
          <line x1="14.5" y1="21.5" x2="17.5" y2="21.5"/>
        </svg>
        <span>(123) 456-7890</span>
      </li>
      <li class="contact-item">
        <svg class="contact-icon" viewBox="0 0 32 32" fill="none" stroke="currentColor" stroke-width="1.4">
          <circle cx="16" cy="16" r="14.5"/>
          <path d="M8.5 13 q7.5 -5 15 0 l-1.5 2.5 -3 -1 v-1.5 q-3 -1 -6 0 v1.5 l-3 1 z"/>
          <rect x="10.5" y="16" width="11" height="7" rx="1"/>
        </svg>
        <span>(123) 456-7890</span>
      </li>
      <li class="contact-item">
        <svg class="contact-icon" viewBox="0 0 32 32" fill="none" stroke="currentColor" stroke-width="1.4">
          <circle cx="16" cy="16" r="14.5"/>
          <rect x="8.5" y="10.5" width="15" height="11"/>
          <polyline points="8.5,10.5 16,17 23.5,10.5"/>
        </svg>
        <span>sales@varnelsupply.example</span>
      </li>
      <li class="contact-item">
        <svg class="contact-icon" viewBox="0 0 32 32" fill="none" stroke="currentColor" stroke-width="1.4">
          <circle cx="16" cy="16" r="14.5"/>
          <circle cx="16" cy="16" r="8"/>
          <ellipse cx="16" cy="16" rx="3.5" ry="8"/>
          <line x1="8" y1="16" x2="24" y2="16"/>
        </svg>
        <span>VarnelSupply.com.au</span>
      </li>
    </ul>

    <p class="brand-name">Varnel Supply</p>
  </div>
</body>
</html>
```